Wren Vehicle Polishing (Mobile detail)

I need a business card made up. I'd like it to be different in some form, either raised, embossed, debossed, something cool that stands out. (preferably embossed text somewhere in it). I will be including the Initial png file. Let me know if you need the photoshop of adobe illustrator file to work with.
Updates

Information to be included: Text: XXX-XXX-XXXX Phone: XXX-XXX-XXXX Email: wrenvehiclepolish@mailnest.example Website: www.socialpage.example/wrenvehiclepolishKTR Hours of operation: Mon - Fri 7:00AM to 8:00PM Sat - 10:00AM to 8:00PM

Target Market(s)

Mobile automotive detailing

Industry/Entity Type

Automotive

Contact Information for Business Card

Make it stand out with embossed lettering, I'd also like the background to be glossy black or matte, something that represents a shiny car, black preferred

Requirements
Must have
• A glossy background, or something.
• My logo, pick one of them that best fits your design.
Should not have
• White background,
• something that does not stand out.

```html
<!DOCTYPE html>
<html lang="en">
<head>
<meta charset="utf-8">
<title>Wren Vehicle Polishing – Business Card</title>
<link href="https://fonts.googleapis.com/css2?family=Open+Sans:wght@400;600&display=swap" rel="stylesheet">
<style>
  :root {
    --stage: #d9d6d1;
    --card-black: #111112;
    --card-matte: #242425;
    --silver-light: #f2f2f2;
    --silver-mid: #9a9a9a;
    --orange: #f08a24;
    --orange-deep: #d8671a;
    --text-light: #e6e6e6;
    --text-muted: #a7a7a7;
  }
  * { box-sizing: border-box; margin: 0; padding: 0; }
  html, body { width: 1200px; height: 780px; overflow: hidden; }
  body {
    background: var(--stage);
    font-family: "Open Sans", Arial, sans-serif;
    position: relative;
  }
  .card {
    position: absolute;
    top: 230px;
    width: 540px;
    height: 320px;
    border-radius: 16px;
    overflow: hidden;
    box-shadow: 0 10px 28px rgba(0,0,0,.35);
  }
  .card-info { left: 45px; background: var(--card-matte); }
  .card-brand { left: 615px; background: var(--card-black); }

  /* contact side */
  .info-swoosh { position: absolute; inset: 0; }
  .person { position: absolute; left: 34px; top: 92px; }
  .person-name { color: var(--orange); font-size: 24px; font-weight: 600; line-height: 1.15; }
  .person-role { color: var(--text-muted); font-size: 16px; line-height: 1.2; }

  .contact { position: absolute; left: 34px; top: 158px; display: flex; gap: 14px; }
  .contact-icons { display: flex; flex-direction: column; gap: 4px; padding-top: 2px; }
  .icon {
    width: 18px; height: 18px; border-radius: 3px;
    background: linear-gradient(var(--orange), var(--orange-deep));
    display: flex; align-items: center; justify-content: center;
  }
  .contact-lines { color: var(--text-light); font-size: 14px; line-height: 22px; }
  .hours {
    position: absolute; left: 66px; top: 256px;
    color: var(--text-light); font-size: 14px; line-height: 22px;
  }

  /* brand side */
  .brand {
    position: absolute; inset: 0;
    display: flex; align-items: center; justify-content: center; gap: 16px;
  }
  .brand-mark {
    width: 54px; height: 54px; border-radius: 50%;
    background: radial-gradient(circle at 35% 30%, var(--silver-light), var(--silver-mid));
  }
  .brand-name { color: var(--text-light); font-size: 30px; font-weight: 600; }
</style>
</head>
<body>
  <section class="card card-info" aria-label="Business card, contact side">
    <svg class="info-swoosh" width="540" height="320" viewBox="0 0 540 320" aria-hidden="true">
      <defs>
        <linearGradient id="silverEdge" x1="0" x2="1">
          <stop offset="0" stop-color="#555"/>
          <stop offset=".5" stop-color="#f2f2f2"/>
          <stop offset="1" stop-color="#777"/>
        </linearGradient>
      </defs>
      <path d="M0 0 H540 V20 C420 95 200 40 0 70 Z" fill="#111112"/>
      <path d="M0 70 C200 40 420 95 540 20" fill="none" stroke="url(#silverEdge)" stroke-width="4"/>
    </svg>

    <div class="person">
      <p class="person-name">Employee Name</p>
      <p class="person-role">Owner</p>
    </div>

    <div class="contact">
      <div class="contact-icons">
        <span class="icon"><svg width="11" height="11" viewBox="0 0 12 12"><path d="M3 1l2 3-1.2 1.2a6 6 0 0 0 3 3L8 7l3 2-1 2C5 11 1 7 1 2z" fill="#222"/></svg></span>
        <span class="icon"><svg width="12" height="10" viewBox="0 0 12 10"><rect x="1" y="1" width="10" height="8" fill="none" stroke="#222" stroke-width="1.4"/><path d="M1 1l5 4 5-4" fill="none" stroke="#222" stroke-width="1.4"/></svg></span>
        <span class="icon"><svg width="12" height="12" viewBox="0 0 12 12"><circle cx="6" cy="6" r="5" fill="none" stroke="#222" stroke-width="1.3"/><path d="M1 6h10M6 1c-3 3-3 7 0 10M6 1c3 3 3 7 0 10" fill="none" stroke="#222" stroke-width="1"/></svg></span>
        <span class="icon"></span>
      </div>
      <div class="contact-lines">
        <p>000-000-0000</p>
        <p>wrenvehiclepolish@mailnest.example</p>
        <p>www.wrenpolish.example</p>
        <p>wrenvehiclepolishKTR</p>
      </div>
    </div>

    <div class="hours">
      <p>Mon - Fri 7:00AM to 8:00PM</p>
      <p>Sat - 10:00AM to 8:00PM</p>
    </div>
  </section>

  <section class="card card-brand" aria-label="Business card, brand side">
    <div class="brand">
      <span class="brand-mark"></span>
      <span class="brand-name">Wren Vehicle Polishing</span>
    </div>
  </section>
</body>
</html>
```